Clever & creative business card needed for a pediatric dentist.

We need a business card for a pediatric dentist that is building a brand-new pediatric dental practice. He is funny, outgoing, and sociable, and he hopes to give his business card to dentists and pediatricians so that he can give them information of where to refer infants, children, and teenagers that need high quality and attainable dental care.

The name of the dental practice is Copper Fern Pediatric Dentistry. Logo design .png / .pdf/ .jpg are provided to aid in the design.

The dentist's last name is Tolvan (which sounds like "burger", as in "hamburger” or “cheeseburger"). Since it is pediatric practice, kudos will be given to designs that implement a little joke into the design - but hopefully in a small or hidden way (such as putting something like a cheeseburger on the back of the card, or hiding it an an abstract way).

Thank you!

Please make a design that incorporates colors. It should be fun! Not too serious. It does not have to follow the color scheme of the logos.

```html
<!DOCTYPE html>
<html lang="en">
<head>
<meta charset="utf-8">
<title>Copper Fern Pediatric Dentistry – Business Card</title>
<link href="https://fonts.googleapis.com/css2?family=Mulish:wght@400;700&display=swap" rel="stylesheet">
<style>
  :root {
    --page: #e6e7e9;
    --card-white: #ffffff;
    --card-dark: #353537;
    --ink: #3a3a3c;
    --green: #5cbf7a;
    --green-light: #a9dbb5;
    --white: #ffffff;
  }
  html, body {
    margin: 0;
    width: 1200px;
    height: 1200px;
    overflow: hidden;
    background: var(--page);
    font-family: "Mulish", sans-serif;
  }
  .stage { position: relative; width: 1200px; height: 1200px; }
  .card {
    position: absolute;
    top: 477px;
    width: 420px;
    height: 240px;
    box-shadow: 8px 8px 10px rgba(0,0,0,0.35);
    overflow: hidden;
  }
  .card--front { left: 202px; background: var(--card-white); color: var(--ink); }
  .card--back { left: 665px; background: var(--card-dark); }

  .brand { position: absolute; left: 16px; top: 17px; width: 134px; text-align: center; }
  .brand__dot {
    display: block; width: 50px; height: 50px; margin: 0 auto 6px;
    border-radius: 50%; background: var(--green-light);
  }
  .brand__name {
    display: block; font-size: 24px; font-weight: 400; line-height: 1;
    color: var(--ink); letter-spacing: 0.5px; white-space: nowrap;
  }
  .brand__tag {
    display: block; font-size: 7px; letter-spacing: 2.6px; margin-top: 5px;
    color: var(--ink); white-space: nowrap;
  }

  .person { position: absolute; left: 258px; top: 74px; }
  .person__name { font-size: 19px; font-weight: 700; color: var(--green); margin: 0; line-height: 1.1; letter-spacing: 0.3px; }
  .person__role { font-size: 12px; margin: 0; line-height: 1.2; }

  .contacts { position: absolute; left: 258px; top: 120px; margin: 0; padding: 0; list-style: none; }
  .contacts li { display: flex; align-items: center; font-size: 12px; height: 14.5px; white-space: nowrap; }
  .contacts svg { width: 10px; height: 10px; margin-right: 6px; flex: none; }

  .rule { position: absolute; left: 16px; top: 189px; width: 389px; height: 1px; background: var(--green); }

  .address { position: absolute; left: 258px; top: 199px; font-size: 12px; line-height: 14px; margin: 0; font-style: normal; }

  .pattern { position: absolute; inset: 0; background: var(--card-dark); }
  .back-brand { position: absolute; left: 0; right: 0; top: 90px; text-align: center; }
  .back-brand .brand__dot { width: 46px; height: 46px; }
  .back-brand .brand__name, .back-brand .brand__tag { color: var(--white); }
  .back-brand .brand__name { font-size: 20px; }
  .back-brand .brand__tag { font-size: 6px; letter-spacing: 2.2px; margin-top: 3px; }
</style>
</head>
<body>
<div class="stage">

  <section class="card card--front">
    <div class="brand">
      <span class="brand__dot"></span>
      <span class="brand__name">copper fern</span>
      <span class="brand__tag">PEDIATRIC DENTISTRY</span>
    </div>

    <div class="person">
      <p class="person__name">John Tolvan</p>
      <p class="person__role">Owner/ CEO</p>
    </div>

    <ul class="contacts">
      <li>
        <svg viewBox="0 0 10 10" aria-hidden="true"><path d="M2 1 L3.5 1 L4.2 3 L3 3.8 Q4 6 6.2 7 L7 5.8 L9 6.5 L9 8 Q8.5 9 7.5 9 Q1 8 1 2 Q1 1 2 1Z" fill="var(--green)"/></svg>
        (09) 5550 1470
      </li>
      <li>
        <svg viewBox="0 0 10 10" aria-hidden="true"><rect x="2.5" y="0.5" width="5" height="9" rx="1" fill="none" stroke="var(--green)" stroke-width="1"/><circle cx="5" cy="8" r="0.5" fill="var(--green)"/></svg>
        (09) 5550 1470
      </li>
      <li>
        <svg viewBox="0 0 10 10" aria-hidden="true"><rect x="0.5" y="2" width="9" height="6" fill="var(--green)"/><path d="M0.5 2 L5 5.5 L9.5 2" fill="none" stroke="#fff" stroke-width="0.8"/></svg>
        john@copperfern.com
      </li>
      <li>
        <svg viewBox="0 0 10 10" aria-hidden="true"><circle cx="5" cy="5" r="4.3" fill="var(--green)"/><path d="M0.7 5 H9.3 M5 0.7 V9.3 M5 0.7 Q2.5 5 5 9.3 M5 0.7 Q7.5 5 5 9.3" fill="none" stroke="#fff" stroke-width="0.6"/></svg>
        www.copperfern.com
      </li>
    </ul>

    <div class="rule"></div>

    <address class="address">0/00 Larkin Ave<br>Brindle Bay, 0000</address>
  </section>

  <section class="card card--back">
    <div class="pattern" role="img" aria-label="Tonal embossed repeat pattern of the practice mark on dark grey"></div>
    <div class="back-brand">
      <span class="brand__dot"></span>
      <span class="brand__name">copper fern</span>
      <span class="brand__tag">PEDIATRIC DENTISTRY</span>
    </div>
  </section>

</div>
</body>
</html>
```